Need a sleek, professional business card design for a Web Development business

I need a unique business card designed for a web development company. It is also the parent company for any ventures I do, such as my ClipWave channel, startup ideas I have, etc. I am the single member of "Bright Harbor Code LLC." I will attach my basic logo here, so you will see the current color scheme and have the asset available. Thank you!

Target Market(s)

Startups, SMB's, Professionals

Industry/Entity Type

Business

Font styles to use
Other font styles liked:
• Lovello for headings is what I use, but not necessary.

Colors

Designer to choose colors to be used in the design.

Requirements
Nice to have
• Sleek is the word. Professional, modern, dark.
Should not have
• Any work from someone else's design. Lacking originality.

```html
<!DOCTYPE html>
<html lang="en">
<head>
<meta charset="utf-8">
<title>Bright Harbor Code LLC – Business Card</title>
<link href="https://fonts.googleapis.com/css2?family=Lato:wght@400;700&display=swap" rel="stylesheet">
<style>
  :root {
    --stage: #2e2e30;
    --card-black: #000000;
    --card-white: #ffffff;
    --accent-orange: #f6935a;
    --accent-pink: #e9566b;
    --text-light: #ffffff;
  }
  * { margin: 0; padding: 0; box-sizing: border-box; }
  html, body {
    width: 1200px; height: 900px; overflow: hidden;
    background: var(--stage);
    font-family: "Lato", Arial, sans-serif;
  }
  .stage { position: relative; width: 1200px; height: 900px; }
  .card {
    position: absolute; left: 250px; width: 700px; height: 400px;
    overflow: hidden;
    box-shadow: 0 10px 30px rgba(0,0,0,.45);
  }
  .card-back { top: 35px; background: var(--card-black); }
  .card-front { top: 465px; background: var(--card-white); }
  .card-art { position: absolute; inset: 0; width: 700px; height: 400px; }

  .brand {
    position: absolute; display: flex; align-items: center; gap: 14px;
    font-weight: 700; font-size: 30px; color: var(--accent-orange);
    white-space: nowrap;
  }
  .brand-dot {
    width: 22px; height: 22px; border-radius: 50%;
    background: var(--accent-orange);
  }
  .card-back .brand { left: 50%; top: 150px; transform: translateX(-50%); }
  .back-url {
    position: absolute; left: 0; right: 0; top: 318px; text-align: center;
    color: var(--text-light); font-size: 19px; letter-spacing: 1.5px;
  }
  .card-front .brand { left: 30px; top: 162px; font-size: 22px; gap: 12px; }
  .card-front .brand-dot { width: 20px; height: 20px; }

  .contact { position: absolute; left: 420px; top: 95px; color: var(--text-light); }
  .contact-name { font-weight: 700; font-size: 32px; color: var(--accent-orange); line-height: 1; white-space: nowrap; }
  .contact-role { font-size: 19px; margin-top: 4px; }
  .contact-address { font-size: 20px; line-height: 1.2; margin-top: 20px; }
  .contact-list { list-style: none; margin-top: 14px; margin-left: -32px; }
  .contact-list li { display: flex; align-items: center; gap: 12px; font-size: 20px; line-height: 1.3; white-space: nowrap; }
  .contact-icon { width: 20px; height: 20px; flex: none; fill: var(--accent-orange); }
</style>
</head>
<body>
<main class="stage">

  <section class="card card-back" aria-label="Card back">
    <div class="brand"><span class="brand-dot"></span>Bright Harbor Code</div>
    <p class="back-url">www.brightharborcode.com</p>
  </section>

  <section class="card card-front" aria-label="Card front">
    <svg class="card-art" viewBox="0 0 700 400" aria-hidden="true">
      <defs>
        <linearGradient id="swoosh-gradient" x1="0" y1="1" x2="0" y2="0">
          <stop offset="0" stop-color="#f6935a"/>
          <stop offset="1" stop-color="#e9566b"/>
        </linearGradient>
      </defs>
      <path d="M440 0 L700 0 L700 400 L190 400 C 240 230 330 90 440 0 Z" fill="#000"/>
      <path d="M205 400 C 255 230 345 90 457 0" fill="none" stroke="#fff" stroke-width="6"/>
      <path d="M420 0 L470 0 C 380 60 310 170 270 330 C 290 190 350 75 420 0 Z" fill="url(#swoosh-gradient)"/>
    </svg>

    <div class="brand"><span class="brand-dot"></span>Bright Harbor Code</div>

    <div class="contact">
      <h1 class="contact-name">Daniel Rourke</h1>
      <p class="contact-role">Manager</p>
      <p class="contact-address">418 Cedar Bend Road<br>Austin, TX 78745</p>
      <ul class="contact-list">
        <li>
          <svg class="contact-icon" viewBox="0 0 20 20" aria-label="Phone"><path d="M4 2 L8 2 L9 6 L7 8 C8 10 10 12 12 13 L14 11 L18 12 L18 16 C18 17 17 18 16 18 C9 18 2 11 2 4 C2 3 3 2 4 2 Z"/></svg>
          512 555 0142
        </li>
        <li>
          <svg class="contact-icon" viewBox="0 0 20 20" aria-label="Fax"><path d="M5 2 H15 V7 H5 Z M2 8 H18 V15 H15 V12 H5 V15 H2 Z M6 13 H14 V18 H6 Z"/></svg>
          512 555 0143
        </li>
        <li>
          <svg class="contact-icon" viewBox="0 0 20 20" aria-label="Email"><path d="M2 4 H18 V16 H2 Z" /><path d="M2 4 L10 11 L18 4" fill="none" stroke="#000" stroke-width="1.5"/></svg>
          info@brightharborcode.com
        </li>
        <li>
          <svg class="contact-icon" viewBox="0 0 20 20" aria-label="Website"><circle cx="10" cy="10" r="8"/><path d="M2 10 H18 M10 2 C6 6 6 14 10 18 M10 2 C14 6 14 14 10 18 M4 6 H16 M4 14 H16" fill="none" stroke="#000" stroke-width="1.2"/></svg>
          www.brightharborcode.com
        </li>
      </ul>
    </div>
  </section>

</main>
</body>
</html>
```